High-Class Professional Letterhead for a solo doctor's practice.

Please create a letterhead design that includes my logo, and options of my light blue/black color scheme and black and gold so I can choose between the two. I would like my Contact information on the top or bottom of the letterhead somewhere:
Delia Forsk, M.D.
Hand and Upper Extremity Surgeon
4382 NW 58th Lane, Suite 307
Tamarac, FL 33498
Phone: (954) 316-8842
Fax: (800) 629-4087
www.dforskgrip.example

Also on the bottom of the letterhead, there should be 2 different versions:
one that is blank, and one that has a signature spot on the bottom so I can sign:
Delia Forsk, M.D.
Board Certified Orthopaedic Hand Surgeon

I am going for classy/professional. I want other doctors and or lawyers to look at my letterhead and want to work with me. Again, professional, classy, clean. I do like black and gold but I could see what the blue like my other business card looks like too. Please do what most people do for letterheads--I'm not sure if the signature line should be on there? Or should be blank? I have no clue

Target Market(s)

Doctors and Lawyers

Industry/Entity Type

Medicine

Colors
0054AA
0677BA
7BADD7
CADEEF
E8F1F8

Requirements
Must have
• High class, professional, appealing

```html
<!DOCTYPE html>
<html lang="en">
<head>
<meta charset="utf-8">
<title>Delia Forsk, M.D. — Letterhead</title>
<link href="https://fonts.googleapis.com/css2?family=Questrial&family=Roboto:wght@400&display=swap" rel="stylesheet">
<style>
  :root {
    --backdrop: #e4e4e4;
    --paper: #f7f7f7;
    --ink: #4a4a4a;
    --ink-soft: #5a5a5a;
    --rule: #c4c4c4;
    --gold: #c6a55f;
    --accent-blue: #0677ba;
  }
  * { margin: 0; padding: 0; box-sizing: border-box; }
  html, body {
    width: 1023px; height: 1200px; overflow: hidden;
    background: var(--backdrop);
  }
  .sheet {
    position: absolute; left: 83px; top: 0;
    width: 856px; height: 1200px;
    background: var(--paper);
    font-family: "Questrial", "Century Gothic", sans-serif;
    color: var(--ink);
  }
  .brand {
    position: absolute; left: 72px; top: 108px;
    display: flex; align-items: center; gap: 10px;
    color: var(--gold);
    font-size: 22px; letter-spacing: 0.5px;
  }
  .brand-dot {
    width: 16px; height: 16px; border-radius: 50%;
    background: var(--gold);
  }
  .contact {
    position: absolute; left: 582px; top: 74px;
    padding-left: 19px; height: 98px;
    border-left: 1px solid var(--rule);
    font-family: "Roboto", Arial, sans-serif;
    font-size: 12.5px; line-height: 15px; color: var(--ink);
  }
  .contact .address { margin-top: 4px; margin-bottom: 7px; }
  .contact .line { display: flex; align-items: center; gap: 6px; height: 17px; }
  .contact svg { width: 12px; height: 12px; flex: none; }
  .letter {
    position: absolute; left: 81px; top: 314px; width: 704px;
  }
  .salutation { font-size: 16px; margin-bottom: 37px; }
  .letter p {
    font-size: 12.6px; line-height: 18.2px; color: var(--ink-soft);
    text-align: justify; margin-bottom: 18px;
  }
  .letter p.gap-before { margin-top: 18px; }
  .closing { position: absolute; left: 81px; top: 810px; font-size: 12.6px; color: var(--ink-soft); }
</style>
</head>
<body>
  <div class="sheet">
    <div class="brand">
      <span class="brand-dot"></span>
      <span class="brand-name">Delia Forsk, M.D.</span>
    </div>

    <div class="contact">
      <div class="address">4382 NW 58th Lane, Suite 307<br>Tamarac, FL 33498</div>
      <div class="line">
        <svg viewBox="0 0 12 12" aria-hidden="true"><path fill="var(--accent-blue)" d="M2.4 1l1.8 2.2-.9 1.3c.7 1.6 2 2.9 3.6 3.6l1.3-.9L10.4 9l-.6 1.7C5.2 10.8 1.2 6.8 1.3 1.6z"/></svg>
        <span>(954) 316-8842</span>
      </div>
      <div class="line">
        <svg viewBox="0 0 12 12" aria-hidden="true"><rect x="3" y="1" width="6" height="3" fill="var(--accent-blue)"/><rect x="1" y="4.5" width="10" height="4.5" rx="1" fill="var(--accent-blue)"/><rect x="3" y="8" width="6" height="3" fill="var(--accent-blue)" opacity=".7"/></svg>
        <span>(800) 629-4087</span>
      </div>
      <div class="line">
        <svg viewBox="0 0 12 12" aria-hidden="true"><circle cx="6" cy="6" r="5.2" fill="var(--accent-blue)"/><path d="M1 6h10M6 1c-2 2.6-2 7.4 0 10M6 1c2 2.6 2 7.4 0 10" stroke="#fff" stroke-width=".8" fill="none"/></svg>
        <span>www.dforskgrip.example</span>
      </div>
    </div>

    <main class="letter">
      <div class="salutation">Dear John,</div>
      <p>Donec malesuada orci vitae nulla accumsan porta a id massa. Quisque accumsan iaculis magna sit amet fringilla. Maecenas consequat, magna eget tincidunt semper, odio nibh rutrum mi, id feugiat ante nisi eu risus. Vestibulum nunc orci, rhoncus a placerat in, ultricies in mi. Cras mattis varius eros, vel fringilla nisi suscipit eget. Quisque scelerisque sagittis nulla at porttitor.</p>
      <p>Lorem ipsum dolor sit amet, consectetur adipiscing elit. Donec orci purus, luctus vitae dignissim eu, iaculis sed purus. Vivamus faucibus, ipsum nec aliquet viverra, leo mauris condimentum ligula, sit amet sagittis enim ligula quis arcu. Nam egestas tortor id nisi porttitor mattis. In tortor ante, ultricies in suscipit a, tempus non massa. Vivamus et auctor mi. Fusce vel massa nulla. Phasellus nec eros mauris, et scelerisque orci.</p>
      <p class="gap-before">It is a long established fact that a reader will be distracted by the readable content of a page when looking at its layout. The point of using Lorem Ipsum is that it has a more-or-less normal distribution of letters, as opposed to using 'Content here, content here', making it look like readable English. Many desktop publishing packages</p>
      <p>Sed id augue vitae urna euismod commodo aliquet a quam. Pellentesque arcu velit, cursus et malesuada ut, consequat et diam. Nullam erat sem, rhoncus id ullamcorper vitae, rhoncus et arcu. In ultricies ultricies nulla, ut rutrum nisi iaculis at. Donec eu magna a metus ornare faucibus. Fusce aliquet faucibus ultricies. Morbi semper, est id tincidunt gravida, sem arcu adipiscing lacus, ac bibendum nulla leo eu purus. Quisque nec diam sed risus consectetur a ccumsan quis quis nibh. Vestibulum id purus lorem.</p>
    </main>

    <div class="closing">Sincerely,</div>
  </div>
</body>
</html>
```